BOOK COVER (6 X 9) FOR HALLMERE COVE BOOKS

Book title: ROADS OF EMBER; Author: TOMAS R. VELDIC

This is the story of a man who grew up in Saudi Arabia in the 1940s, was schooled around the world. He survived death many times, once during the revolution in Bangladesh in the 1970s. Although a Pakistani, he knew Saudi royalty and worked there for most of his life. A lot of mystical things happened to him. SORRY TO BE SO VAGUE.

Book size will be 6 x 9

Target Market(s)

Adults interested in immigrant stories; the unexplainable; whimsical memoirs

Requirements
Nice to have
• This is a man who lived in many different worlds and countries. He lived through the Bangladesh revolution and other life threatening events.
Should not have
• Arabic dress -- he wore white suits

```html
<!DOCTYPE html>
<html lang="en">
<head>
<meta charset="utf-8">
<title>Roads of Ember — Hallmere Cove Books</title>
<link rel="stylesheet" href="https://fonts.googleapis.com/css2?family=Cormorant:wght@700&family=Tinos&display=swap">
<style>
  :root {
    --sky-top: #8f9aa4;
    --sky-mid: #6d7781;
    --water-dark: #3b3a38;
    --marsh: #5b5246;
    --rule: #f3efe9;
    --paper-light: #f2ede6;
    --paper-mid: #d9cfc3;
    --sepia: #a58c74;
    --sepia-dark: #7a634f;
    --ink: #161210;
    --author: #3f2d21;
    --imprint: #ffffff;
  }
  * { margin: 0; padding: 0; box-sizing: border-box; }
  html, body { width: 800px; height: 1200px; overflow: hidden; background: var(--paper-light); }
  .cover { position: relative; width: 800px; height: 1200px; overflow: hidden; }

  .imprint-band {
    position: absolute; top: 0; left: 0; width: 800px; height: 320px;
    background: linear-gradient(180deg, var(--sky-top) 0%, var(--sky-mid) 24%, var(--water-dark) 38%, var(--marsh) 52%, #6f655a 66%, #8a8177 82%, #a39b91 100%);
    border-bottom: 6px solid var(--rule);
  }
  .imprint-name {
    position: absolute; top: 128px; left: 0; width: 800px; text-align: center;
    font-family: "Tinos", "Times New Roman", serif; color: var(--imprint);
    font-size: 54px; line-height: 64px; letter-spacing: 4px;
  }

  .cover-art {
    position: absolute; top: 326px; left: 0; width: 800px; height: 874px;
    background:
      radial-gradient(ellipse 70% 40% at 85% 18%, rgba(120,110,104,0.45), transparent 70%),
      radial-gradient(ellipse 60% 45% at 10% 95%, var(--sepia-dark), transparent 70%),
      linear-gradient(180deg, var(--paper-light) 0%, var(--paper-mid) 45%, var(--sepia) 80%, var(--sepia-dark) 100%);
  }

  .title {
    position: absolute; top: 0; left: 0; width: 800px; text-align: center;
    font-family: "Cormorant", "Times New Roman", serif; font-weight: 700;
    color: var(--ink); font-size: 220px; line-height: 1;
  }
  .title-line {
    position: absolute; left: 0; width: 800px; display: block;
    transform: scaleX(0.56); transform-origin: center;
  }
  .title-line--first { top: 435px; }
  .title-line--second { top: 635px; }

  .author {
    position: absolute; top: 1056px; left: 0; width: 800px; text-align: center;
    font-family: "Tinos", "Times New Roman", serif; color: var(--author);
    font-size: 38px; letter-spacing: 3px;
  }
</style>
</head>
<body>
<main class="cover">
  <header class="imprint-band" role="img" aria-label="Photograph of a misty coastal marsh at dusk"></header>
  <p class="imprint-name">HALLMERE COVE BOOKS</p>

  <section class="cover-art" role="img" aria-label="Faded sepia map outline of the Arabian Peninsula with drifting clouds"></section>

  <h1 class="title">
    <span class="title-line title-line--first">ROADS</span>
    <span class="title-line title-line--second">OF EMBER</span>
  </h1>
  <p class="author">TOMAS R. VELDIC</p>
</main>
</body>
</html>
```